Webpage Toggle Button Graphics

We are a webhosting company that sells Hosted Servers (Windows/Linux etc). We have for each service in our catalogue a number of on/off/maybe toggle buttons (not actally buttons, but display). Out current design is not modern enough, and would like a new design for the concept. (current screenshot is attached).
Updates

It seems I need to clarify something.  The ICONS I need are for the Buttons in the attachment marked Anti-virus, File Backup, HIDS, DR.  Not anything else on the page. The New icons do need to fit in with the look and feel of the page, and ideally are smaller (so we can fit more of these ICONS on the page). Thanks              

Industry/Entity Type

It Company

Requirements
Must have
• Generic Button Display, with 4 states- ON (Red/Bad, I have this feature), OFF (Green/Good, I do not have this feature), N/A (greyed out, feature is not available), MAYBE (Blue, I dont have this feature but its not really Red/Bad)
• Prefer a generic version with a single visual cue (dot/button or whatever) and a Text Description (i.e. not a custom ICON for each feature)
• Needs to fit in the space similiar to the screenshot, but Ideally smaller.
• Initial buttons are to be for:
• Anti-Virus (AV)
• Backup (Back)
• Host Intrusion Detection (HIDS)
• Disaster Recovery (DR)
• DDOS (DDOS)
• Can submittions be in the format of the attachment with your designs embedded into the picture to show what it will look like in production. May Icon 1-RED, 2, Green, 3 Blue, 4 - Greyed out.
Nice to have
• Ideally the button/display is generic, and our developers can just add the text for any future buttons

```html
<!DOCTYPE html>
<html lang="en">
<head>
<meta charset="utf-8">
<title>Toggle Switch Set</title>
<link rel="stylesheet" href="https://fonts.googleapis.com/css2?family=Open+Sans:wght@600;700;800&display=swap">
<style>
:root{
  --bg:#e9ecec;
  --bg-edge:#d9dddd;
  --green:#8fd22a;
  --green-text:#3b6a06;
  --red:#ef4d4d;
  --red-text:#7a0f0f;
  --pink:#ffb3b8;
  --blue:#2aa2e0;
  --blue-dark:#137dbb;
  --magenta:#d23b8e;
  --white:#ffffff;
  --grey:#cfd1d1;
  --grey-dark:#9a9c9c;
  --ink:#4a4a4a;
  --ink-soft:#a5a5a5;
  --charcoal:#2e2e2e;
  --frame:#1d1d1d;
}
*{box-sizing:border-box;margin:0;padding:0}
html,body{width:1200px;height:600px;overflow:hidden}
body{
  background:radial-gradient(ellipse at center,var(--bg) 40%,var(--bg-edge) 100%);
  font-family:"Open Sans",Arial,sans-serif;
  position:relative;
}
.toggle{position:absolute}
.label{font-weight:800;text-transform:uppercase;letter-spacing:.5px;white-space:nowrap}

/* pill switches */
.pill{
  width:176px;height:60px;border-radius:30px;padding:5px;
  background:linear-gradient(#b5b8b8,#f4f5f5);
  box-shadow:0 2px 3px rgba(0,0,0,.25) inset,0 1px 0 #fff;
}
.pill .track{
  width:100%;height:100%;border-radius:25px;position:relative;
  display:flex;align-items:center;
  box-shadow:0 2px 4px rgba(0,0,0,.35) inset;
}
.pill.on .track{background:linear-gradient(#aee552,var(--green) 55%,#76b81a);padding-left:34px}
.pill.off .track{background:linear-gradient(#ff7b7b,var(--red) 55%,#d73636);padding-left:82px}
.pill .label{font-size:25px}
.pill.on .label{color:var(--green-text)}
.pill.off .label{color:var(--red-text)}
.pill .knob{
  position:absolute;top:1px;width:48px;height:48px;border-radius:50%;
  background:linear-gradient(#fbfbfb,#c9cbcb);
  box-shadow:0 2px 4px rgba(0,0,0,.45);
}
.pill.on .knob{right:1px}
.pill.off .knob{left:1px}
.pill .knob::after{
  content:"";position:absolute;left:20px;top:20px;width:8px;height:8px;border-radius:50%;
  background:#555;box-shadow:0 1px 0 #fff;
}

/* compact icon switches */
.mini{
  width:134px;height:50px;border-radius:25px;padding:4px;
  background:linear-gradient(#c9cbcb,#f5f6f6);
  box-shadow:0 1px 3px rgba(0,0,0,.3) inset,0 1px 0 #fff;
}
.mini .track{width:100%;height:100%;border-radius:21px;position:relative;box-shadow:0 2px 3px rgba(0,0,0,.3) inset}
.mini.on .track{background:linear-gradient(#b6ef55,var(--green))}
.mini.off .track{background:linear-gradient(#ffc8cc,var(--pink))}
.mini .knob{
  position:absolute;top:0;width:72px;height:42px;border-radius:21px;
  background:linear-gradient(#ffffff,#dcdede);box-shadow:0 2px 4px rgba(0,0,0,.35);
}
.mini .knob::before,.mini .knob::after{
  content:"";position:absolute;top:11px;width:4px;height:20px;border-radius:2px;background:#c4c6c6;
}
.mini .knob::before{left:30px}.mini .knob::after{left:38px}
.mini.on .knob{right:0}
.mini.off .knob{left:0}
.mini svg{position:absolute;top:11px;width:20px;height:20px}
.mini.on svg{left:16px}
.mini.off svg{right:18px}

/* segmented light switches */
.seg{
  width:188px;height:60px;padding:3px;border-radius:3px;
  background:linear-gradient(#8a8c8c,#c9cbcb);
  box-shadow:0 3px 5px rgba(0,0,0,.35);display:flex;
}
.seg .part{flex:1;display:flex;align-items:center;justify-content:center;font-size:22px}
.seg .light{background:linear-gradient(#ffffff,#eeeeee)}
.seg .dim{background:linear-gradient(#f0f0f0,#e2e2e2);color:var(--ink-soft)}
.seg .on-text{color:#3f8a0c}
.seg .off-text{color:#c61f1f}
.seg .blue{background:linear-gradient(#3bb3ef,var(--blue-dark));color:var(--white)}
.seg .magenta{background:linear-gradient(#e255a2,var(--magenta));color:var(--white)}
.grip{display:flex;gap:6px}
.grip i{display:block;width:4px;height:18px;border-radius:2px}
.grip.blue-grip i{background:var(--blue)}
.grip.pink-grip i{background:var(--magenta)}

/* segmented dark switches */
.dark{
  width:170px;height:64px;border-radius:8px;padding:3px;display:flex;
  background:linear-gradient(#9a9c9c,#d4d6d6);box-shadow:0 2px 3px rgba(0,0,0,.3);
}
.dark .part{flex:1;display:flex;align-items:center;justify-content:center;font-size:22px}
.dark .part:first-child{border-radius:6px 0 0 6px}
.dark .part:last-child{border-radius:0 6px 6px 0}
.dark .grey{background:linear-gradient(#d9dbdb,#c3c5c5);color:var(--ink)}
.dark .black{background:linear-gradient(#3c3c3c,#222);box-shadow:0 2px 5px rgba(0,0,0,.6) inset}
.dark .black.go{color:var(--green)}
.dark .black.stop{color:#ff5a5a}

/* approve / reject */
.choice{
  width:264px;height:58px;border-radius:6px;padding:5px;display:flex;gap:4px;
  background:linear-gradient(#3a3a3a,var(--frame));box-shadow:0 3px 5px rgba(0,0,0,.4);
}
.choice .part{
  flex:1;border-radius:3px;display:flex;align-items:center;justify-content:center;gap:6px;font-size:15px;
}
.choice .raised{background:linear-gradient(#ffffff,#e6e6e6)}
.choice .sunk{background:linear-gradient(#b9bbbb,#a3a5a5);color:var(--charcoal);box-shadow:0 1px 3px rgba(0,0,0,.5) inset}
.choice .approve{color:#3f8a0c}
.choice .reject{color:#c61f1f}
.choice svg{width:12px;height:12px}

/* four-state feature indicators */
.features{position:absolute;left:115px;top:470px;display:flex;gap:30px}
.feature{
  width:170px;height:48px;border-radius:24px;padding:4px;
  background:linear-gradient(#c9cbcb,#f5f6f6);
  box-shadow:0 1px 3px rgba(0,0,0,.3) inset,0 1px 0 #fff;
}
.feature .track{
  width:100%;height:100%;border-radius:20px;display:flex;align-items:center;gap:12px;padding:0 4px;
  box-shadow:0 2px 3px rgba(0,0,0,.3) inset;
}
.feature .dot{
  width:32px;height:32px;border-radius:50%;flex:none;position:relative;
  background:linear-gradient(#ffffff,#d6d8d8);box-shadow:0 2px 3px rgba(0,0,0,.35);
}
.feature .dot::after{content:"";position:absolute;left:12px;top:12px;width:8px;height:8px;border-radius:50%}
.feature .label{font-size:18px;color:var(--white);text-shadow:0 1px 1px rgba(0,0,0,.25)}
.feature.bad .track{background:linear-gradient(#ff7b7b,var(--red) 55%,#d73636)}
.feature.bad .dot::after{background:var(--red)}
.feature.good .track{background:linear-gradient(#aee552,var(--green) 55%,#76b81a)}
.feature.good .dot::after{background:#5f9a12}
.feature.good .label{color:var(--green-text);text-shadow:none}
.feature.maybe .track{background:linear-gradient(#3bb3ef,var(--blue-dark))}
.feature.maybe .dot::after{background:var(--blue)}
.feature.na .track{background:linear-gradient(#e2e3e3,var(--grey))}
.feature.na .dot::after{background:var(--grey-dark)}
.feature.na .label{color:var(--ink-soft);text-shadow:none}
</style>
</head>
<body>

<div class="toggle pill on" style="left:66px;top:140px"><div class="track"><span class="label">On</span><span class="knob"></span></div></div>
<div class="toggle pill off" style="left:312px;top:140px"><div class="track"><span class="knob"></span><span class="label">Off</span></div></div>

<div class="toggle mini on" style="left:686px;top:148px"><div class="track">
  <svg viewBox="0 0 20 20"><path d="M3 10 l5 5 L17 4" fill="none" stroke="#2f6d04" stroke-width="4" stroke-linecap="round" stroke-linejoin="round"/></svg>
  <span class="knob"></span></div></div>
<div class="toggle mini off" style="left:898px;top:148px"><div class="track">
  <span class="knob"></span>
  <svg viewBox="0 0 20 20"><path d="M5 5 L15 15 M15 5 L5 15" stroke="#d41f2b" stroke-width="4" stroke-linecap="round"/></svg></div></div>

<div class="toggle seg" style="left:48px;top:250px"><span class="part light label on-text">On</span><span class="part dim label">Off</span></div>
<div class="toggle seg" style="left:312px;top:250px"><span class="part dim label">On</span><span class="part light label off-text">Off</span></div>

<div class="toggle dark" style="left:636px;top:254px"><span class="part grey label">Off</span><span class="part black go label">On</span></div>
<div class="toggle dark" style="left:904px;top:254px"><span class="part black stop label">Off</span><span class="part grey label">On</span></div>

<div class="toggle seg" style="left:48px;top:364px"><span class="part light"><span class="grip blue-grip"><i></i><i></i><i></i></span></span><span class="part blue label">Yes</span></div>
<div class="toggle seg" style="left:312px;top:364px"><span class="part magenta label">No</span><span class="part light"><span class="grip pink-grip"><i></i><i></i><i></i></span></span></div>

<div class="toggle choice" style="left:560px;top:366px">
  <span class="part raised label approve"><svg viewBox="0 0 12 12"><path d="M1 6 l3 3 L11 2" fill="none" stroke="currentColor" stroke-width="2.5"/></svg>Approve</span>
  <span class="part sunk label"><svg viewBox="0 0 12 12"><path d="M2 2 L10 10 M10 2 L2 10" stroke="currentColor" stroke-width="2.5"/></svg>Reject</span>
</div>
<div class="toggle choice" style="left:902px;top:366px">
  <span class="part sunk label"><svg viewBox="0 0 12 12"><path d="M1 6 l3 3 L11 2" fill="none" stroke="currentColor" stroke-width="2.5"/></svg>Approve</span>
  <span class="part raised label reject"><svg viewBox="0 0 12 12"><path d="M2 2 L10 10 M10 2 L2 10" stroke="currentColor" stroke-width="2.5"/></svg>Reject</span>
</div>

<div class="features">
  <div class="feature bad"><div class="track"><span class="dot"></span><span class="label">AV</span></div></div>
  <div class="feature good"><div class="track"><span class="dot"></span><span class="label">Backup</span></div></div>
  <div class="feature maybe"><div class="track"><span class="dot"></span><span class="label">HIDS</span></div></div>
  <div class="feature na"><div class="track"><span class="dot"></span><span class="label">DR</span></div></div>
  <div class="feature bad"><div class="track"><span class="dot"></span><span class="label">DDOS</span></div></div>
</div>

</body>
</html>
```